Kestrel Bridge Consulting (KBC) Business Card Design

I would like to create double-sided business cards that contain:
1) Name: Derek Molvane
2) Phone Number: +1 (555) 218-4907
3) Email: Derek.Molvane@KestrelBridgeConsulting.example
4) Website: KestrelBridgeConsulting.example

I would like to include my logo and a color scheme similar to the Varnholt Grand Prix Ostera squad color scheme (black, silver, greenish-blue – but can also include regular blue)

What we do: Our company develops and delivers innovative and pragmatic information technology and cybersecurity risk and compliance solutions for organizations in the commercial market as well as the federal, and state/local sectors.

```html
<!DOCTYPE html>
<html lang="en">
<head>
<meta charset="utf-8">
<title>Kestrel Bridge Consulting – Business Cards</title>
<link rel="stylesheet" href="https://fonts.googleapis.com/css2?family=Roboto+Condensed:wght@400;700&family=Roboto:wght@400&display=swap">
<style>
  :root {
    --backdrop: #8e8e8c;
    --paper: #ffffff;
    --night: #0c1120;
    --brand-blue: #1663b0;
    --brand-teal: #35b7ae;
    --ink-grey: #5b5f66;
    --rule-grey: #4a4d52;
    --silver: #8f98ac;
  }
  * { box-sizing: border-box; margin: 0; padding: 0; }
  html, body { width: 1200px; height: 801px; overflow: hidden; }
  body {
    background: var(--backdrop);
    font-family: "Roboto", Arial, sans-serif;
    position: relative;
  }
  .card {
    position: absolute;
    top: 252px;
    width: 520px;
    height: 297px;
    overflow: hidden;
    border-bottom: 3px solid var(--brand-blue);
    border-right: 2px solid var(--brand-blue);
    box-shadow: 0 6px 16px rgba(0,0,0,.25);
  }
  .card--front { left: 54px; background: var(--paper); }
  .card--back { left: 626px; background: var(--night); }

  .brand {
    position: absolute;
    display: flex;
    align-items: center;
    gap: 16px;
  }
  .brand__dot {
    width: 62px; height: 62px;
    border-radius: 50%;
    flex: none;
  }
  .brand__name {
    font-family: "Roboto Condensed", Arial, sans-serif;
    font-weight: 400;
    text-transform: uppercase;
    letter-spacing: 3px;
    font-size: 25px;
    line-height: 1.05;
  }
  .card--front .brand { left: 40px; top: 52px; }
  .card--front .brand__dot { background: var(--brand-teal); }
  .card--front .brand__name {
    color: var(--rule-grey);
    border-left: 1px solid var(--rule-grey);
    padding-left: 12px;
  }

  .holder {
    position: absolute;
    left: 40px;
    right: 24px;
    bottom: 60px;
    display: flex;
    align-items: center;
  }
  .holder__name {
    font-family: "Roboto Condensed", Arial, sans-serif;
    font-weight: 700;
    font-size: 22px;
    color: var(--brand-blue);
    text-transform: uppercase;
    white-space: nowrap;
    padding-right: 14px;
  }
  .holder__rule {
    width: 1px;
    height: 70px;
    background: var(--brand-blue);
    margin-right: 12px;
    flex: none;
  }
  .contact { list-style: none; min-width: 0; }
  .contact li {
    display: flex;
    align-items: center;
    gap: 6px;
    font-size: 11px;
    color: var(--ink-grey);
    line-height: 20px;
    white-space: nowrap;
  }
  .contact svg { width: 11px; height: 11px; flex: none; }

  .card--back .brand { left: 72px; top: 100px; }
  .card--back .brand__dot { background: #050811; box-shadow: inset 0 0 0 1px #1b2233; }
  .card--back .brand__name {
    color: var(--silver);
    border-left: 1px solid #3a4152;
    padding-left: 14px;
    font-size: 30px;
  }
</style>
</head>
<body>
  <section class="card card--front" aria-label="Business card front">
    <div class="brand">
      <span class="brand__dot"></span>
      <p class="brand__name">Kestrel<br>Bridge<br>Consulting</p>
    </div>
    <div class="holder">
      <p class="holder__name">Derek Molvane</p>
      <span class="holder__rule"></span>
      <ul class="contact">
        <li>
          <svg viewBox="0 0 12 12" aria-hidden="true"><path d="M3 1l2 2.5-1.2 1.3a7 7 0 0 0 3.4 3.4L8.5 7 11 9l-1.4 2C5 11 1 7 1 2.4z" fill="var(--brand-teal)"/></svg>
          +1 (555) 218-4907
        </li>
        <li>
          <svg viewBox="0 0 12 12" aria-hidden="true"><rect x="1" y="2.5" width="10" height="7" fill="var(--brand-teal)"/><path d="M1 2.5l5 4 5-4" stroke="#fff" fill="none"/></svg>
          Derek.Molvane@KestrelBridgeConsulting.example
        </li>
        <li>
          <svg viewBox="0 0 12 12" aria-hidden="true"><circle cx="6" cy="6" r="5" fill="var(--brand-teal)"/><path d="M1 6h10M6 1c-2.5 3-2.5 7 0 10M6 1c2.5 3 2.5 7 0 10" stroke="#fff" stroke-width=".8" fill="none"/></svg>
          KestrelBridgeConsulting.example
        </li>
      </ul>
    </div>
  </section>

  <section class="card card--back" aria-label="Business card back">
    <div class="brand">
      <span class="brand__dot"></span>
      <p class="brand__name">Kestrel<br>Bridge<br>Consulting</p>
    </div>
  </section>
</body>
</html>
```